Professional and modern website for Real Estate services company

Hi there! We're looking for a responsive, highly professional and modern (in line with Latest trends) coded website for a Real Estate services company named Portalia720º (find logo attached). I will try to Explain how I picture it in my head, but feel free to step out of the script and design it as you please. The structure for the website must be as Follows: - Menu: at the top of the screen, always visible (in any page and when to scrolling down). Logo at the left hand side (clicking redirects to home), then a Services, About us, Blog and Contact and on the right hand, Estimate and Log in (just placeholder, no log in required yet). - Home: (I like https://fr.domvera.example/): a landscape picture of Madrid's skyline. Very important That at a first glance (without scrolling) you can see a box to input data of your building to get an estimate (Post code, Number of homes, Number of garages, Number of stores, Swimming pool (yes / no) Concierge (yes / no)). Should there be a small space Also for a corporate presentation video (more or less like https://www.velbrastahogares.example/ but With the estimate Request box INSTEAD OF the App - however, do not take this one as example Given I just wanted to illustrate the structure). Still in the Home, bellow the first glance, I'd like to have a brief introduction of the following pages (Services, About us, Blog and Contact). This can be in a Either "square" form (like https://fr.domvera.example/) or in a "scroll" form (like https://k7pisos.example/). - Services: we offer 3 sets of services, each of them composed by three specific services, Namely: * Administration Treasury Accounting Savings * Consulting Legal Technical Regulatory * Mediation Repairs Meetings Delinquency For the sake of structuring, each of the nine services will Have to written description composed of 3 small paragraphs of About 15 words. I Tend to like to Accompany With each of the services related icons / vectors, but feel free to design them as you want. - About us: content not yet defined, but will be a series of bullets / sections in Which We talk about prep or differentiating points. We can include the corporate video presentation here again. - Blog: just a space Where you can see to the blog entries (in Home, probably just show 3/4). - Contact: a fancy contact form, with map, address, telephone, e-mail and opening hours. Just to give it a bit more content, maybe include a catch phrase like "We're looking forward to meeting you!" or something like that. - Estimate: this is the Most Important page in the website (in Addition to the upper part of the Home page). Basically replicate the estimate for the home box, but maybe with a bit more design or extended, Given this is a single page just for that. - Log in: opens a drop-down with user and password (just placeholder, no log in required yet). Regarding colors, we still do not Have a color scheme, so anything in line With the logo is OK. Many thanks in advance, Martin

All ages and genders

Real Estate

Coded - Design and coding required

5+ page

Sans Serif

Must have
• Blank colored background

```html
<!DOCTYPE html>
<html lang="en">
<head>
<meta charset="utf-8">
<title>portalia720 – Real Estate Services</title>
<link href="https://fonts.googleapis.com/css2?family=Roboto:wght@300;400;500;700&display=swap" rel="stylesheet">
<style>
:root{
  --orange:#d06b0b;
  --orange-light:#e07a12;
  --dark:#221a14;
  --darker:#1a130e;
  --ink:#3a3a3a;
  --body:#555;
  --white:#fff;
  --grey-band:#dcdcdc;
  --line:#bdbdbd;
}
*{margin:0;padding:0;box-sizing:border-box}
html,body{width:1200px;height:2329px;overflow:hidden;background:#fff;font-family:"Roboto",Arial,sans-serif;color:var(--body)}
.page{position:relative;width:1200px;height:2329px}
.abs{position:absolute}

/* header */
.site-header{position:absolute;left:0;top:0;width:1200px;height:100px;background:#fff}
.brand{position:absolute;left:95px;top:30px;display:flex;align-items:center;gap:10px;font-size:34px;font-weight:700;color:var(--ink);letter-spacing:-0.5px}
.brand-mark{width:14px;height:14px;background:var(--orange)}
.main-nav{position:absolute;left:447px;top:41px;display:flex;gap:0}
.main-nav a{font-size:12px;font-weight:500;color:#222;text-decoration:none;text-transform:uppercase;margin-right:46px;padding-bottom:6px}
.main-nav a.active{color:var(--orange);border-bottom:1px solid var(--orange)}
.btn-login,.btn-estimate{position:absolute;top:31px;height:36px;font-size:12px;font-weight:500;color:#fff;display:flex;align-items:center;justify-content:center;text-transform:uppercase}
.btn-login{left:871px;width:102px;background:var(--orange)}
.btn-estimate{left:981px;width:125px;background:var(--dark)}

/* hero */
.hero{position:absolute;left:0;top:100px;width:1200px;height:527px;background:linear-gradient(180deg,#b66a6e 0%,#e79a4a 30%,#c9622a 55%,#7a3420 80%,#4a2418 100%)}
.hero-title{position:absolute;left:0;top:322px;width:1020px;text-align:center;color:#fff;font-size:52px;font-weight:500;line-height:54px;text-shadow:0 2px 6px rgba(0,0,0,.45)}

/* estimate */
.estimate{position:absolute;left:93px;top:510px;width:1014px;height:227px;background:var(--dark)}
.estimate h2{position:absolute;left:42px;top:22px;font-size:25px;font-weight:500;color:var(--orange-light)}
.estimate .rule{position:absolute;left:42px;top:60px;width:930px;height:1px;background:#5a4a3d}
.field{position:absolute;width:158px;border-bottom:1px solid #7a6a5d;color:#e8e8e8;font-size:13px;padding-bottom:7px}
.field.select::after{content:"";position:absolute;right:4px;top:6px;border:4px solid transparent;border-top-color:#bbb}
.toggle-label{position:absolute;color:#e8e8e8;font-size:13px}
.toggle{position:absolute;width:34px;height:12px;border-radius:6px;background:#8a8a8a}
.toggle::after{content:"";position:absolute;right:-2px;top:-4px;width:20px;height:20px;border-radius:50%;background:#fff}
.submit{position:absolute;left:856px;top:96px;width:120px;height:81px;background:var(--orange);color:#fff;font-size:19px;font-weight:500;line-height:21px;display:flex;align-items:center;justify-content:center;text-align:center}

/* sections */
.section-title{position:absolute;font-size:37px;font-weight:400;color:var(--ink)}
.section-title span{color:var(--orange);font-weight:500}
.lead{position:absolute;font-size:14.5px;line-height:21px;color:var(--body)}
.ticks{position:absolute;list-style:none;font-size:13px;color:#444}
.ticks li{height:32px;display:flex;align-items:flex-start;gap:10px}
.ticks svg{margin-top:2px}
.video{position:absolute;left:700px;top:778px;width:407px;height:239px;background:radial-gradient(circle at 60% 50%,#3a3e45 0%,#1d2025 70%)}
.play{position:absolute;left:160px;top:82px;width:78px;height:78px;border-radius:50%;background:#fff;border:6px solid rgba(120,120,120,.7)}

.services-band{position:absolute;left:0;top:1082px;width:1200px;height:489px;background:linear-gradient(180deg,#d4d4d4 0%,#e6e6e6 50%,#cfcfcf 100%)}
.card{position:absolute;top:1268px;width:320px;height:206px;border:1px solid #b9b9b9;background:rgba(255,255,255,.25)}
.card-tab{position:absolute;left:-1px;top:-1px;width:58px;height:55px;background:var(--orange);border-bottom-right-radius:55px}
.card h3{position:absolute;left:64px;top:16px;font-size:21px;font-weight:400;color:#333}
.card ul{position:absolute;left:64px;top:54px;width:230px;list-style:none}
.card li{height:46px;display:flex;align-items:center;gap:12px;border-bottom:1px solid #c4c4c4;font-size:17px;color:var(--orange)}
.card li:last-child{border-bottom:none}
.svc-icon{width:36px;height:36px;border-radius:50%;background:#4a4a4a;display:flex;align-items:center;justify-content:center;flex:none}

.post-img{position:absolute;top:1769px;width:234px;height:159px}
.date{position:absolute;left:0;top:0;width:42px;height:42px;background:var(--orange);color:#fff;font-size:11px;font-weight:700;line-height:14px;padding:7px 0 0 8px}
.post-title{position:absolute;top:1766px;width:250px;font-size:20px;line-height:26px;color:#222}
.post-text{position:absolute;top:1860px;width:240px;font-size:13px;line-height:21px;color:#666}

/* footer */
.site-footer{position:absolute;left:0;top:2021px;width:1200px;height:256px;background:linear-gradient(180deg,#3a2a1b 0%,#2c2016 100%)}
.footer-col{position:absolute;top:58px;color:#eee}
.footer-col h4{font-size:14px;font-weight:700;text-transform:uppercase;padding-bottom:10px;border-bottom:1px solid #6a5a4c;margin-bottom:14px}
.quick a{display:block;color:#eee;text-decoration:none;font-size:12px;line-height:22px;text-transform:uppercase}
.quick a::before{content:"▸ ";font-size:9px}
.contact-row{display:flex;gap:10px;font-size:12.5px;line-height:17px;margin-bottom:14px}
.news p{font-size:10.5px;line-height:16px;color:#ddd;width:240px}
.news .email{margin-top:14px;font-size:10.5px;border-bottom:1px solid #ddd;width:213px;padding-bottom:6px}
.news .subscribe{margin-top:15px;display:inline-block;background:var(--orange);color:#fff;font-size:10px;padding:4px 8px;text-transform:uppercase}
.social div{display:flex;align-items:center;gap:10px;font-size:12.5px;height:34px}
.social i{width:24px;height:24px;background:#777}
.copyright{position:absolute;left:0;top:2277px;width:1200px;height:52px;background:var(--darker);color:#9a8a7c;font-size:10.5px;display:flex;align-items:center;justify-content:center}
</style>
</head>
<body>
<div class="page">

<header class="site-header">
  <div class="brand"><span>portalia720</span><span class="brand-mark"></span></div>
  <nav class="main-nav">
    <a class="active">Home</a><a>Services</a><a>About us</a><a>Blog</a><a>Contact</a>
  </nav>
  <div class="btn-login">Login</div>
  <div class="btn-estimate">Free Estimate</div>
</header>

<section class="hero" role="img" aria-label="Photograph of the Madrid skyline at sunset">
</section>
<h1 class="hero-title">Going Above and Beyond<br>to Find Your Next Home</h1>

<form class="estimate">
  <h2>Get an Free Estimate</h2>
  <div class="rule"></div>
  <svg class="abs" style="left:930px;top:36px" width="45" height="26" viewBox="0 0 45 26"><path d="M2 25 V12 L22 2 L43 12 V25" fill="none" stroke="#6a5a4d" stroke-width="1.5"/></svg>
  <div class="field" style="left:42px;top:96px">Your Name</div>
  <div class="field" style="left:250px;top:96px">Your Email ID</div>
  <div class="field select" style="left:456px;top:96px">Number of Garages</div>
  <div class="field" style="left:42px;top:161px">Post Code</div>
  <div class="field select" style="left:250px;top:161px">Number of Homes</div>
  <div class="field select" style="left:456px;top:161px">Number of Stores</div>
  <div class="toggle-label" style="left:664px;top:104px">Swimming Pool</div>
  <div class="toggle" style="left:787px;top:106px"></div>
  <div class="toggle-label" style="left:664px;top:158px">Concierge</div>
  <div class="toggle" style="left:787px;top:160px"></div>
  <div class="submit">SUBMIT<br>NOW</div>
</form>

<h2 class="section-title" style="left:93px;top:778px">about <span>portalia720</span></h2>
<p class="lead" style="left:93px;top:837px;width:540px;font-size:13px;line-height:21px">Lorem ipsum dolor sit amet, consectetur adipisicing elit, sed do eiusmod tempor ut incididunt labore et dolore magna aliqua. Ut enim ad minim veniam, quis nostrud exercitation ullamco laboris nisi ut aliquip ex ea commodo consequat.</p>
<ul class="ticks" style="left:93px;top:927px">
  <li><svg width="11" height="10"><path d="M1 5 L4 8 L10 1" fill="none" stroke="#d06b0b" stroke-width="2"/></svg>Lorem ipsum dolor sit amet</li>
  <li><svg width="11" height="10"><path d="M1 5 L4 8 L10 1" fill="none" stroke="#d06b0b" stroke-width="2"/></svg>Phasellus leo augue, cursus sed</li>
  <li><svg width="11" height="10"><path d="M1 5 L4 8 L10 1" fill="none" stroke="#d06b0b" stroke-width="2"/></svg>Aliquam quis felis fringilla</li>
</ul>
<ul class="ticks" style="left:372px;top:927px">
  <li><svg width="11" height="10"><path d="M1 5 L4 8 L10 1" fill="none" stroke="#d06b0b" stroke-width="2"/></svg>Lorem ipsum dolor sit amet</li>
  <li><svg width="11" height="10"><path d="M1 5 L4 8 L10 1" fill="none" stroke="#d06b0b" stroke-width="2"/></svg>Phasellus leo augue, cursus sed</li>
  <li><svg width="11" height="10"><path d="M1 5 L4 8 L10 1" fill="none" stroke="#d06b0b" stroke-width="2"/></svg>Aliquam quis felis fringilla</li>
</ul>
<div class="video" role="img" aria-label="Corporate presentation video still of hands holding a small house">
  <div class="play"><svg style="position:absolute;left:24px;top:19px" width="20" height="28"><path d="M2 2 L18 14 L2 26 Z" fill="#d06b0b"/></svg></div>
</div>

<section class="services-band" role="img" aria-label="Faded photograph of a classic city building framed by trees"></section>
<h2 class="section-title" style="left:93px;top:1116px">our <span>services</span></h2>
<p class="lead" style="left:93px;top:1172px;width:1010px">Lorem ipsum dolor sit amet, consectetur adipisicing elit, sed do eiusmod tempor ut incididunt labore et dolore magna aliqua. Ut enim ad minim veniam, quis nostrud exercitation ullamco laboris nisi ut aliquip ex ea commodo consequat.</p>

<div class="card" style="left:93px">
  <div class="card-tab"><svg style="position:absolute;left:14px;top:12px" width="22" height="22" viewBox="0 0 22 22"><circle cx="11" cy="6" r="5" fill="#fff"/><path d="M1 21 C1 13 21 13 21 21 Z" fill="#fff"/></svg></div>
  <h3>Administration</h3>
  <ul>
    <li><span class="svc-icon"><svg width="16" height="16"><rect x="2" y="9" width="3" height="6" fill="#fff"/><rect x="7" y="5" width="3" height="10" fill="#fff"/><rect x="12" y="1" width="3" height="14" fill="#fff"/></svg></span>Treasury</li>
    <li><span class="svc-icon" style="color:#fff;font-size:15px">%</span>Accounting</li>
    <li><span class="svc-icon"><svg width="16" height="16"><circle cx="8" cy="9" r="6" fill="#fff"/></svg></span>Savings</li>
  </ul>
</div>
<div class="card" style="left:440px">
  <div class="card-tab"><span style="position:absolute;left:19px;top:6px;color:#fff;font-size:26px;font-weight:700">i</span></div>
  <h3>Consulting</h3>
  <ul>
    <li><span class="svc-icon"><svg width="16" height="16"><rect x="3" y="3" width="8" height="4" fill="#fff" transform="rotate(-35 7 5)"/><rect x="2" y="13" width="12" height="2" fill="#fff"/></svg></span>Legal</li>
    <li><span class="svc-icon"><svg width="18" height="18"><circle cx="9" cy="9" r="6" fill="none" stroke="#fff" stroke-width="3"/></svg></span>Technical</li>
    <li><span class="svc-icon"><svg width="10" height="18"><rect x="1" y="1" width="8" height="16" rx="2" fill="#fff"/></svg></span>Regulatory</li>
  </ul>
</div>
<div class="card" style="left:786px">
  <div class="card-tab"><svg style="position:absolute;left:14px;top:12px" width="22" height="22" viewBox="0 0 22 22"><circle cx="11" cy="6" r="5" fill="#fff"/><path d="M1 21 C1 13 21 13 21 21 Z" fill="#fff"/></svg></div>
  <h3>Mediation</h3>
  <ul>
    <li><span class="svc-icon"><svg width="16" height="16"><path d="M3 13 L10 6" stroke="#fff" stroke-width="3"/><circle cx="11" cy="5" r="3.5" fill="#fff"/></svg></span>Repairs</li>
    <li><span class="svc-icon"><svg width="18" height="16"><circle cx="5" cy="4" r="3" fill="#fff"/><circle cx="13" cy="4" r="3" fill="#fff"/><rect x="2" y="8" width="6" height="7" fill="#fff"/><rect x="10" y="8" width="6" height="7" fill="#fff"/></svg></span>Meetings</li>
    <li><span class="svc-icon"><svg width="18" height="18"><circle cx="9" cy="9" r="7" fill="none" stroke="#fff" stroke-width="1.5"/><circle cx="9" cy="9" r="4" fill="none" stroke="#fff" stroke-width="1.5"/></svg></span>Delinquency</li>
  </ul>
</div>

<h2 class="section-title" style="left:93px;top:1618px">recent <span>blog post</span></h2>
<p class="lead" style="left:93px;top:1676px;width:1010px">Lorem ipsum dolor sit amet, consectetur adipisicing elit, sed do eiusmod tempor ut incididunt labore et dolore magna aliqua. Ut enim ad minim veniam, quis nostrud exercitation ullamco laboris nisi ut aliquip ex ea commodo consequat.</p>

<article>
  <div class="post-img" style="left:93px;background:linear-gradient(160deg,#c9b48a 0%,#5a4a32 55%,#2e2a22 100%)" role="img" aria-label="Photograph of a house among trees in morning light">
    <div class="date">10<br>DEC</div>
  </div>
  <h3 class="post-title" style="left:353px">Aliquam quis felis fringilla, pretium ante sit amet, sagittis nunc.</h3>
  <p class="post-text" style="left:353px">Nam vehicula augue ac ex tincidunt, quis tristique dolor ullamcorper. Donec gravida neque cursus</p>
</article>
<article>
  <div class="post-img" style="left:613px;background:linear-gradient(150deg,#9a8a7a 0%,#c7b9a8 50%,#6a5a4a 100%)" role="img" aria-label="Photograph of colleagues reviewing plans on a table">
    <div class="date">09<br>DEC</div>
  </div>
  <h3 class="post-title" style="left:873px">Cum sociis natoque penatibus et magnis dis parturient montes,</h3>
  <p class="post-text" style="left:873px">Nam vehicula augue ac ex tincidunt, quis tristique dolor ullamcorper. Donec gravida neque cursus</p>
</article>

<footer class="site-footer" role="contentinfo">
  <div class="footer-col quick" style="left:100px;width:170px">
    <h4>Quick Links</h4>
    <a>Home</a><a>About</a><a>Services</a><a>Blog</a><a>Contact us</a>
  </div>
  <div class="footer-col" style="left:323px;width:284px">
    <h4>Contact Information</h4>
    <div class="contact-row"><svg width="10" height="14"><path d="M5 13 C1 8 1 6 1 5 A4 4 0 0 1 9 5 C9 6 9 8 5 13Z" fill="#fff"/></svg><span>2260 Alder Row Suite 14 Brenfield,<br>TX 70412</span></div>
    <div class="contact-row"><svg width="10" height="14"><path d="M6 1 C2 3 2 11 6 13" fill="none" stroke="#fff" stroke-width="2.5"/></svg><span>555-014-7720</span></div>
    <div class="contact-row"><svg width="11" height="14"><rect x="0" y="3" width="11" height="8" fill="#fff"/></svg><span>info@portalia720.example</span></div>
  </div>
  <div class="footer-col news" style="left:660px;width:242px">
    <h4>Newsletter Signup</h4>
    <p>Please enter your email address below to receive our FREE newsletter</p>
    <div class="email">Your Email ID</div>
    <span class="subscribe">Subscribe</span>
  </div>
  <div class="footer-col social" style="left:953px;width:187px">
    <h4>Follow us</h4>
    <div><i></i>Friendwall</div>
    <div><i></i>Workmesh</div>
    <div><i></i>Chirper</div>
    <div><i></i>Email</div>
  </div>
</footer>
<div class="copyright">Copyright© 2016 portalia720. All Rights Received</div>

</div>
</body>
</html>
```